Reaching the Right Campus Might Be Simpler Than Expected! Nine Moves Toward Stronger Report Cards...

I need a cover/front/spine/back for an e-book and a hard cover book that I am publishing on Zembrix. I have written a book with an eight step process on how to help parents coach their kids to getting grades up and accepted into good colleges. In the book, I am highlighting current day struggles teens and young adults are having with mental health due to the impact of social media. I am helping them understand the impact mental health and social media has had on school stress. I outline a process in my book that my reader can implement herself with her child, or hire me as her coach.

Target Market(s)

Women ages 35 to 55 with teens in high school and college

Industry/Entity Type

Life Coaching

Font styles to use
Serif

Colors

Designer to choose colors to be used in the design.

Requirements
Must have
• Title, name, (credentials/PhD) and simple image on cover. Font and
• point size that you can read in a teeny, tiny thumbnail. Readability is number one goal. Text on thumbnail must be readable. I have been made aware that subtitles are hard to get on E-books.
Nice to have
• Something that immediately lets the reader know what my book is about
Should not have
• No italics or swirly curly font.

```html
<!DOCTYPE html>
<html lang="en">
<head>
<meta charset="utf-8">
<title>Reaching the Right Campus Might Be Simpler Than Expected! – Book Cover</title>
<link rel="stylesheet" href="https://fonts.googleapis.com/css2?family=Old+Standard+TT:wght@400;700&family=Questrial&display=swap">
<style>
  :root {
    --page-bg: #ffffff;
    --cover-cream: #fdfaec;
    --title-gold: #d9a23a;
    --subtitle-brown: #6b4a2e;
    --cap-dark: #1f1f1f;
    --cap-mid: #3a3a3a;
    --cap-label: #ffffff;
  }
  * { box-sizing: border-box; margin: 0; padding: 0; }
  html, body {
    width: 1200px;
    height: 1106px;
    overflow: hidden;
    background: var(--page-bg);
  }
  .canvas {
    position: relative;
    width: 1200px;
    height: 1106px;
  }
  .book-cover {
    position: absolute;
    left: 300px;
    top: 53px;
    width: 600px;
    height: 1000px;
    background: var(--cover-cream);
    display: flex;
    flex-direction: column;
    align-items: center;
    padding: 70px 30px 50px;
    font-family: "Old Standard TT", Georgia, serif;
    color: var(--title-gold);
    text-align: center;
  }
  .title {
    display: flex;
    flex-direction: column;
    align-items: center;
    font-weight: 400;
    line-height: 0.95;
    white-space: nowrap;
  }
  .title-line { display: block; }
  .title-line--reaching { font-size: 92px; }
  .title-line--emblem-row {
    display: flex;
    align-items: center;
    gap: 24px;
    margin: 4px 0 -6px;
  }
  .emblem {
    position: relative;
    width: 270px;
    height: 140px;
    border-radius: 10px;
    background: linear-gradient(160deg, var(--cap-mid), var(--cap-dark));
    display: flex;
    align-items: flex-end;
    justify-content: center;
    padding-bottom: 28px;
  }
  .emblem-label {
    font-family: "Old Standard TT", Georgia, serif;
    font-weight: 700;
    font-size: 40px;
    color: var(--cap-label);
  }
  .title-line--right { font-size: 86px; }
  .title-line--campus { font-size: 120px; font-weight: 700; }
  .title-line--might { font-size: 72px; font-weight: 700; }
  .title-line--simpler { font-size: 58px; margin-top: 6px; }
  .title-line--expected { font-size: 68px; margin-top: 6px; }
  .subtitle {
    margin-top: 34px;
    font-size: 24px;
    color: var(--subtitle-brown);
  }
  .author {
    margin-top: auto;
    font-family: "Questrial", Arial, sans-serif;
    font-size: 28px;
    color: var(--subtitle-brown);
  }
</style>
</head>
<body>
<div class="canvas">
  <section class="book-cover">
    <h1 class="title">
      <span class="title-line title-line--reaching">REACHING</span>
      <span class="title-line title-line--emblem-row">
        <span class="emblem" role="img" aria-label="Graduation cap with a rolled diploma tied with a red ribbon">
          <span class="emblem-label">THE</span>
        </span>
        <span class="title-line--right">RIGHT</span>
      </span>
      <span class="title-line title-line--campus">CAMPUS</span>
      <span class="title-line title-line--might">MIGHT BE</span>
      <span class="title-line title-line--simpler">SIMPLER THAN</span>
      <span class="title-line title-line--expected">EXPECTED!</span>
    </h1>
    <p class="subtitle">Nine Moves Toward Stronger Report Cards...</p>
    <p class="author">Author Name/PhD</p>
  </section>
</div>
</body>
</html>
```